Dental Transition Company Needs Design for Table top Display at Tradeshows

We need a Graphic Design for a Table Top Display that is used at Trade-shows we attend.
A little bit about what we do: We are a Dental Transitions company, we help new and retiring dentists buy or sell their dental practices. Think of it as a real-estate broker for Dental businesses. Some of the things that Transitions include are practice valuations, which is a determination of how much that practice is worth in respect the the amount of business that comes through on a yearly basis. We also help dentists find associates, or help new graduates find associateships.
KRL Dental Transitions was founded by Martin F. Ellery, whom is an attorney in the dental field, who brings a new perspective to the dental transition experience due to his legal background.
About the project: We have a table top display called an Vantor QS-4 (Spec sheet attatched, but don't worry, the printers will do all the cutting and printing..but this will let you see how the actual display is divided, however, the image should be one cohesive image), it consists of 5 (3 main and two very small side) panels made from vinyl. Here are the approx. specs of the display.
Height: 1.51 m
59.5''
Width: 2.44 m
96''
Depth: 0.52 m
20.4''
Our printers request Vector graphics or EPS, and the color mode must be Pantone / PMS Spot Color
What we would like to see: We need our company logo, motto "We are here to guide you through"
Colors: Deep Burgundy, White, Grey, and Black
A list of our services: Practice Sales, Buyer Representation, Seller Representation, Practice Valuations, Associateships
We need the font to be large and clear, easy to read, because people are going to be walking by this display, you need to be able to read it quick! We are open to creative design Ideas!
View our website to see more about out and our general marketing image: www.ellerypracticeguides.example
Please add in www.krltransitions.example to the image (this website is not live yet but will be soon)
Updates
Our sliders were accidentally incorrect, the design slider was all the way to "feminine" but we need the design to appeal to both men, and women equally. It has been updated. Thank you
Target Market(s)
Our market is largely retiring dentists, and also new dentists looking to start.
Industry/Entity Type
Marketing
Requirements
Must have
- Must have company logo, name, motto, website and list of services.
Services are: Practice Valuations, Practice Sales, Buyer Representation, Seller Representation, Associateships.
Please remake logo into vector format as well to go along with the vector format (but keep it as close to the original as possible)
Should not have
- No teeth please :)

```html
<!DOCTYPE html>
<html lang="en">
<head>
<meta charset="utf-8">
<title>KRL Dental Transitions – Table Top Display</title>
<link rel="stylesheet" href="https://fonts.googleapis.com/css2?family=Sorts+Mill+Goudy&family=Cabin:wght@400;500&display=swap">
<style>
  :root {
    --burgundy: #300510;
    --burgundy-ink: #3a0a14;
    --logo-ink: #24060c;
    --grey-band: #7b7b7b;
    --grey-text: #8c8c8c;
    --ink: #1a1a1a;
    --white: #ffffff;
    --stage: #e9e9e9;
    --photo-dark: #2c2c30;
    --photo-light: #d9d3cf;
  }
  * { margin: 0; padding: 0; box-sizing: border-box; }
  html, body {
    width: 1200px; height: 997px; overflow: hidden;
    background: var(--stage);
  }
  .display {
    position: absolute; left: 0; top: 127px;
    width: 1200px; height: 742px;
    background: var(--white);
    font-family: "Sorts Mill Goudy", Georgia, serif;
    color: var(--ink);
  }
  .brand {
    position: absolute; left: 36px; top: 52px;
    font-size: 54px; line-height: 1; color: var(--logo-ink);
    white-space: nowrap;
  }
  .motto {
    position: absolute; left: 700px; top: 66px; width: 245px;
    font-family: "Cabin", Arial, sans-serif;
    font-size: 20px; line-height: 29px; text-align: center;
    color: var(--burgundy-ink);
  }
  .team-photo {
    position: absolute; left: 978px; top: 28px;
    width: 170px; height: 272px; border-radius: 60px 60px 8px 8px;
    background: linear-gradient(180deg, var(--photo-light) 0%, var(--photo-dark) 45%, var(--photo-dark) 100%);
  }
  .accent-bar {
    position: absolute; left: 38px; top: 167px;
    width: 50px; height: 353px;
    background: linear-gradient(90deg, var(--burgundy) 0%, #6b3a45 35%, var(--white) 100%);
  }
  .copy { position: absolute; left: 99px; top: 168px; width: 1010px; }
  .copy h2 {
    font-weight: 400; font-size: 22px; color: var(--grey-text);
    margin-bottom: 30px;
  }
  .copy p { font-size: 24px; line-height: 30px; }
  .copy .soft { color: var(--grey-text); }
  .copy .help { margin-top: 28px; }
  .services-band {
    position: absolute; left: 0; top: 537px; width: 1200px; height: 85px;
    background: var(--grey-band); color: var(--white);
    font-size: 22px; display: flex; align-items: center; justify-content: center;
  }
  .footer-band {
    position: absolute; left: 0; top: 622px; width: 1200px; height: 120px;
    background: var(--burgundy); color: var(--white);
  }
  .website {
    position: absolute; left: 100px; top: 32px;
    font-family: "Cabin", Arial, sans-serif; font-weight: 500;
    font-size: 41px; letter-spacing: 0.5px;
  }
  .contact {
    position: absolute; left: 1006px; top: 20px;
    font-family: "Cabin", Arial, sans-serif;
    font-size: 11px; line-height: 14px; font-style: normal;
  }
</style>
</head>
<body>
  <main class="display">
    <div class="brand">KRL Dental Transitions</div>
    <p class="motto">“We are here to guide you through”</p>
    <div class="team-photo" role="img" aria-label="Photograph of the three-person team standing together in business attire"></div>

    <div class="accent-bar"></div>
    <section class="copy">
      <h2>Who are We?</h2>
      <p>KRL Dental Transitions has been providing dental brokerage services since 2009.<br>
        <span class="soft">President and owner, Martin F. Ellery</span>, ESQ, has worked exclusively in the<br>
        dental industry providing consulting and legal services since 2006.</p>
      <h2 class="help">How Can We Help?</h2>
      <p>We are dedicated to utilizing the newest and most effective ways to help you realize your<br>
        practice transition goals. Whether it is selling your existing practice, seeking the right practice<br>
        to purchase, or entering into an associateship, <span class="soft">we can help you reach your goals.</span></p>
    </section>

    <div class="services-band">Our Services: Practice Sales/ Buyer Representation/ Seller Representation/ Practice Valuations/ Associate ships</div>

    <footer class="footer-band">
      <div class="website">www.krltransitions.example</div>
      <address class="contact">
        42 Larkspur Ave.<br>
        Suite C.<br>
        Dunmore, NC 28090<br>
        555-014-2286<br>
        555-014-9930 (FAX)<br>
        mellery@ellerylegal.example
      </address>
    </footer>
  </main>
</body>
</html>
```